New Wipes designs - elegant and nice

3 Variants

1. Baby Wipes - Need optons (Blue and Pink colour for Unisex)
2. Mackup Remover - Pink (or you can advice)
3. Abaya Remover - Black or Purple (or you can advice)

Brief for Baby wipes
- Velour Meadow (logo)
- BABY WIPES (nice baby font)
- Eliminates 99% of germs and bacterias, giving healthy and soft skin

Brief for Makeup Remover
- Velour Meadow (logo)
- Makeup Remover
- Special ultra soft formula which gently cleanses and removes makeup and waterproof mascara for the soft skin.

Brief for Baby wipes
- Velour Meadow (logo)
- Abaya Cleaner
- Dummy copy Dummy copy Dummy copy Dummy copy

Mandatory for all wipes
• dermatology tested icon or word
• ph 5.5
• No Alcohol

Target Market(s)

Arab modern women and Asians

Industry/Entity Type

Baby

Requirements
Must have
• Should be feminine and looks elegant, modern, can add premium baby images/ model face where makeup removal effect and abayas... give little tint of arabic pattern.
Nice to have
• you can advice from your side

```html
<!DOCTYPE html>
<html lang="en">
<head>
<meta charset="utf-8">
<title>Velour Meadow Wet Wipes – Pack Designs</title>
<link rel="stylesheet" href="https://fonts.googleapis.com/css2?family=Fredoka:wght@500&family=Ubuntu:wght@400;500&family=Open+Sans:wght@400;600&family=Cookie&family=Courgette&display=swap">
<style>
:root{
  --page:#ffffff;
  --baby-blue:#2a86d4;
  --baby-pink:#e7a9cf;
  --baby-red:#d42a3a;
  --logo-red:#b5142c;
  --gold:#d9a441;
  --night:#0b0908;
  --plum:#5a2a8a;
  --lilac:#e8d8f0;
  --pink-text:#d4267a;
  --white:#ffffff;
}
*{box-sizing:border-box;margin:0;padding:0}
html,body{width:1200px;height:720px;overflow:hidden;background:var(--page)}
body{position:relative;font-family:"Open Sans",sans-serif}

.pack{position:absolute;overflow:hidden}
.pack::before,.pack::after{content:"";position:absolute;top:0;bottom:0;width:10px;z-index:5;
  background:repeating-linear-gradient(180deg,rgba(255,255,255,.35) 0 3px,rgba(0,0,0,.12) 3px 6px)}
.pack::before{left:0}.pack::after{right:0}

.photo{position:absolute;top:0;bottom:0;right:0}
.peel{position:absolute;top:0;right:0;width:44px;height:44px;z-index:3;
  background:linear-gradient(225deg,var(--page) 0 50%,#dcdcdc 50% 58%,transparent 58%)}
.count{position:absolute;top:12px;right:50px;text-align:center;line-height:1;z-index:4;color:var(--white)}
.count .num{display:block;font-family:"Courgette",cursive;font-size:30px}
.count .unit{display:block;font-size:11px;margin-top:2px}

.brand{position:absolute;display:flex;align-items:center;gap:7px;
  font-family:"Ubuntu",sans-serif;font-weight:500;font-size:27px;white-space:nowrap}
.brand .dot{width:12px;height:12px;border-radius:50%}

.ph{position:absolute;width:48px;height:48px;border-radius:50%;color:var(--white);
  background:var(--badge);border:2px solid var(--white);box-shadow:0 0 0 2px var(--badge);
  font-family:"Courgette",cursive;font-size:15px;line-height:15px;text-align:center;padding-top:7px}
.ph span{display:block}
.seal{position:absolute;width:40px;height:40px;border-radius:50%;
  background:var(--badge);border:3px solid var(--white);box-shadow:0 0 0 2px var(--badge)}
.alcohol{position:absolute;font-family:"Courgette",cursive;font-size:22px;white-space:nowrap}
.tagline{position:absolute;text-align:center;font-size:11.5px;line-height:16px}

/* Baby wipes */
.pack-baby{--badge:var(--baby-red);left:30px;top:40px;width:548px;height:312px;
  background:radial-gradient(circle at 30% 50%,#fff 0 30%,transparent 31%),
  radial-gradient(circle at 30% 50%,transparent 0 33%,#9fd3f2 34% 40%,transparent 41%),
  linear-gradient(100deg,#fbe9f3 0%,#f7d3e6 55%,var(--baby-pink) 100%)}
.pack-baby .photo{left:340px;background:radial-gradient(circle at 45% 55%,#f7d9c6 0 30%,#f4f1ee 55%,#ead7e4 100%)}
.pack-baby .brand{left:58px;top:78px;color:var(--logo-red)}
.pack-baby .brand .dot{background:var(--logo-red)}
.baby-title{position:absolute;left:38px;top:128px;font-family:"Fredoka",sans-serif;font-weight:500;
  font-size:46px;color:var(--baby-blue);white-space:nowrap}
.pack-baby .tagline{left:36px;top:198px;width:270px;color:var(--baby-red)}
.pack-baby .ph{left:300px;top:180px}
.pack-baby .alcohol{left:95px;top:248px;color:var(--baby-blue)}
.pack-baby .seal{left:258px;top:250px}

/* Abaya cleaner */
.pack-abaya{--badge:var(--gold);left:597px;top:40px;width:563px;height:325px;
  background:radial-gradient(ellipse at 42% 40%,#6a4a1e 0%,#2a1c0c 35%,var(--night) 65%)}
.pack-abaya .photo{left:330px;background:linear-gradient(90deg,rgba(11,9,8,0) 0%,#3a2a1f 25%,#c89a80 50%,#2a2220 80%,#151210 100%)}
.pack-abaya .brand{left:70px;top:72px;color:var(--gold)}
.pack-abaya .brand .dot{background:var(--gold)}
.abaya-title{position:absolute;left:22px;top:150px;font-family:"Cookie",cursive;font-size:58px;
  color:var(--gold);white-space:nowrap;line-height:1}
.pack-abaya .tagline{left:26px;top:206px;width:270px;color:var(--white);font-size:12px}
.pack-abaya .ph{left:320px;top:188px}
.pack-abaya .alcohol{left:95px;top:248px;color:var(--gold)}
.pack-abaya .seal{left:286px;top:246px}

/* Makeup remover */
.pack-makeup{--badge:var(--plum);left:325px;top:360px;width:565px;height:330px;
  background:radial-gradient(circle at 22% 40%,#fff 0 26%,transparent 27%),
  radial-gradient(circle at 22% 40%,transparent 0 30%,rgba(195,90,184,.55) 31% 40%,transparent 41%),
  linear-gradient(100deg,#f4e6f4 0%,var(--lilac) 45%,#9a6bc0 100%)}
.pack-makeup .photo{left:390px;background:radial-gradient(ellipse at 55% 45%,#e9c2a8 0 30%,#c9a0b8 60%,#8e62b4 100%)}
.pack-makeup .brand{left:90px;top:88px;color:var(--logo-red)}
.pack-makeup .brand .dot{background:var(--logo-red)}
.makeup-title{position:absolute;left:18px;top:150px;font-family:"Ubuntu",sans-serif;font-weight:400;
  font-size:34px;color:var(--plum);white-space:nowrap}
.pack-makeup .tagline{left:16px;top:202px;width:290px;color:var(--pink-text);font-size:11px;line-height:15px}
.pack-makeup .ph{left:330px;top:180px}
.pack-makeup .alcohol{left:105px;top:262px;color:var(--plum)}
.pack-makeup .seal{left:290px;top:244px}
</style>
</head>
<body>

<section class="pack pack-baby">
  <div class="photo" role="img" aria-label="Smiling baby wrapped in a white towel"></div>
  <div class="peel"></div>
  <div class="count"><span class="num">72</span><span class="unit">wipes</span></div>
  <div class="brand"><span class="dot"></span>Velour Meadow</div>
  <h1 class="baby-title">Baby Wipes</h1>
  <p class="tagline">Eliminates 99% of germs and bacterias<br>Giving healthy and soft skin</p>
  <div class="ph"><span>ph</span><span>5.5</span></div>
  <p class="alcohol">Alcohol Free</p>
  <div class="seal" role="img" aria-label="Dermatology tested seal"></div>
</section>

<section class="pack pack-abaya">
  <div class="photo" role="img" aria-label="Woman in a black embroidered abaya and headscarf"></div>
  <div class="peel"></div>
  <div class="count"><span class="num">24</span><span class="unit">pieces</span></div>
  <div class="brand"><span class="dot"></span>Velour Meadow</div>
  <h1 class="abaya-title">Abaya Cleaner</h1>
  <p class="tagline">Cleaning Wet Wipes. Easy &amp; Quick Clean</p>
  <div class="ph"><span>ph</span><span>5.5</span></div>
  <p class="alcohol">Alcohol Free</p>
  <div class="seal" role="img" aria-label="Dermatology tested seal"></div>
</section>

<section class="pack pack-makeup">
  <div class="photo" role="img" aria-label="Woman with clean glowing skin touching her face"></div>
  <div class="peel"></div>
  <div class="count"><span class="num">72</span><span class="unit">wipes</span></div>
  <div class="brand"><span class="dot"></span>Velour Meadow</div>
  <h1 class="makeup-title">Makeup Remover</h1>
  <p class="tagline">Special ultra soft formula which gently cleanses<br>and removes makeup and waterproof mascara<br>for the soft skin</p>
  <div class="ph"><span>ph</span><span>5.5</span></div>
  <p class="alcohol">Alcohol Free</p>
  <div class="seal" role="img" aria-label="Dermatology tested seal"></div>
</section>

</body>
</html>
```